Business branding (card, web design) needed for Remedial / Sports massage

I need a clean, fresh design for my sports massage business called Brightwell-Motion.

I work with high profile professional sports teams (massage, clinical tapeing, health assessments, pilates, coaching) however would like to expand into the entertainment market so need a design that would appeal to both.
NO LOTUS FLOWERS, HANDS OR YOGA POSES FOR DESIGNS

The successful brand design will need to be scalable (e.g. resolution/sizing) to work holistically across my website, marketing collateral and clothing.

Colour pallets that appeal to me - Black, white, blue, green, taupe,
and would prefer clean crisp designs that evoke professionalism, continuous improvement, flow and balance.

Good Luck, can't wait to find my new brand... :)
Updates

I have uploaded a business card that I do like,  See if you can be creative with the logo

Thanks

Target Market(s)

professional sports teams / athletes, and entertainment professionals.

I HAVE UPLOADED A PDF OF WHAT I HAVE DONE. YOU MAY USE LOGO BUT BE CREATIVE PLEASE.

Industry/Entity Type

Entertainment

Contact Information for Business Card

Brightwell-Motion
'Recover Strong' (strap line)

Colette Farrow
Director / Remedial Massage

0417263950
212 Larkmore Street
Kelbridge, VIC 3261

www.brightwell-motion.com.au
info@brightwell-motion.com.au

Logo Text

Brightwell-Motion

Logo styles of interest
Pictorial/Combination Logo
Abstract Logo
Requirements
Should not have
• FLOWERS

```html
<!DOCTYPE html>
<html lang="en">
<head>
<meta charset="utf-8">
<title>Brightwell-Motion — Business Card</title>
<link rel="stylesheet" href="https://fonts.googleapis.com/css2?family=Roboto:wght@300&family=Roboto+Condensed:wght@400;700&display=swap">
<style>
  :root {
    --card-grey: #7a7a78;
    --band-dark: #6f6f6d;
    --band-light: #7d7d7b;
    --text-white: #ffffff;
    --accent-teal: #2ed3cf;
    --rule-grey: #d6d6d6;
  }
  * { margin: 0; padding: 0; box-sizing: border-box; }
  html, body {
    width: 1200px;
    height: 693px;
    overflow: hidden;
  }
  body { background: var(--card-grey); }
  .card {
    position: relative;
    width: 1200px;
    height: 693px;
    background: var(--card-grey);
    color: var(--text-white);
    overflow: hidden;
  }
  .texture-band {
    position: absolute;
    left: 0;
    width: 100%;
  }
  .texture-band--top {
    top: 0;
    height: 180px;
    background: linear-gradient(180deg, var(--band-dark) 0%, var(--band-light) 75%, var(--card-grey) 100%);
  }
  .texture-band--bottom {
    bottom: 0;
    height: 187px;
    background: linear-gradient(0deg, var(--band-dark) 0%, var(--band-light) 80%, var(--card-grey) 100%);
  }
  .brand {
    position: absolute;
    left: 41px;
    top: 280px;
    width: 540px;
  }
  .brand-name {
    font-family: 'Roboto', Arial, sans-serif;
    font-weight: 300;
    font-size: 62px;
    line-height: 1;
    letter-spacing: -1.5px;
    white-space: nowrap;
  }
  .brand-tagline {
    margin-top: 20px;
    font-family: 'Roboto', Arial, sans-serif;
    font-weight: 300;
    font-size: 37px;
    line-height: 1;
    letter-spacing: 0.42em;
    white-space: nowrap;
  }
  .contact {
    position: absolute;
    left: 599px;
    font-family: 'Roboto Condensed', Arial Narrow, sans-serif;
    font-size: 38px;
    line-height: 57px;
    white-space: nowrap;
  }
  .contact--person { top: 248px; }
  .contact--online { top: 550px; line-height: 53px; }
  .person-name {
    font-family: 'Roboto', Arial, sans-serif;
    font-weight: 300;
    font-size: 49px;
    line-height: 54px;
    color: var(--accent-teal);
  }
  .person-role {
    font-weight: 700;
    display: flex;
    align-items: center;
  }
  .role-divider {
    display: inline-block;
    width: 2px;
    height: 26px;
    margin: 0 17px;
    background: var(--rule-grey);
  }
</style>
</head>
<body>
  <main class="card">
    <div class="texture-band texture-band--top" role="img" aria-label="Embossed hexagon texture band"></div>
    <div class="texture-band texture-band--bottom" role="img" aria-label="Embossed hexagon texture band"></div>

    <section class="brand">
      <h1 class="brand-name">Brightwell-Motion</h1>
      <p class="brand-tagline">Recover Strong</p>
    </section>

    <section class="contact contact--person">
      <p class="person-name">Colette Farrow</p>
      <p class="person-role">Director<span class="role-divider"></span>Remedial Massage</p>
      <p class="address-line">212 Larkmore Street Kelbridge</p>
      <p class="address-line">VIC 3261</p>
    </section>

    <section class="contact contact--online">
      <p class="web">www.brightwell-motion.com.au</p>
      <p class="email">info@brightwell-motion.com.au</p>
    </section>
  </main>
</body>
</html>
```